New Menu for Elegant Cafe Pastry Shop

We need to choose a design and layout for our new menu. We would like to also condense our current menu to 4-6 pages.
We will be changing prices and items on the menu, so it needs to be editable. Adobe formats are preferred. The size of the pages needs to be letter size. We will be printing it in house
Please take inspiration from the photos of our shop and food and also our Instagram page.
Attached are our current menu our logo and the logo info

https://www.snapgrid.example/brioweldon/?hl=en
https://maps.example-locate.net/qT7mWx2KpLr9vBn4C

Industry/Entity Type

Food Cafe Bakery pastry

Font styles to use
Other font styles liked:
• please look at attached files

Colors

Designer to choose colors to be used in the design.

Requirements
Nice to have
• Use of Arches like on our shop wallpaper or oblong eclair shapes, Art Deco elements

```html
<!DOCTYPE html>
<html lang="en">
<head>
<meta charset="utf-8">
<title>Brio Weldon — Menu Pages</title>
<link href="https://fonts.googleapis.com/css2?family=Josefin+Sans:wght@300;400;600&family=Poiret+One&family=Cormorant+Garamond:wght@400;500&display=swap" rel="stylesheet">
<style>
:root{
  --teal:#2a8794;
  --teal-dark:#1f6f7a;
  --mist:#d3ecea;
  --gold:#b47d3c;
  --amber:#c98a3e;
  --cream:#fbf6ee;
  --sky:#3db5c8;
  --ink:#3a3532;
  --sand:#e2c08e;
}
*{box-sizing:border-box;margin:0;padding:0}
html,body{width:840px;height:1200px;overflow:hidden;background:#fff}
.sheet{position:relative;width:840px;height:1200px;background:#fff}
.page{position:absolute;width:286px;height:370px;background:var(--frame)}
.page.teal{--frame:var(--teal)}
.page.gold{--frame:var(--gold)}
.field{position:absolute;inset:8px;background:var(--field,var(--mist))}
.page.gold .field{--field:var(--cream)}
.arch{position:absolute;inset:6px 6px;border-radius:50%/26%;background:var(--cream);border:1.2px solid var(--gold);overflow:hidden}
.page.gold .arch{border:5px solid var(--gold);box-shadow:0 0 0 1px var(--teal)}
.arch.mist{background:var(--mist)}
.abs{position:absolute}
.center{text-align:center}
.logo{position:absolute;top:20px;left:0;right:0;display:flex;justify-content:center;align-items:center;gap:3px}
.logo .dot{width:7px;height:7px;border-radius:50%;background:var(--teal)}
.logo .name{font:600 7px 'Josefin Sans',sans-serif;color:var(--teal);letter-spacing:.8px}
.title{font:400 14px 'Josefin Sans',sans-serif;color:var(--gold);letter-spacing:.4px;text-align:center;left:0;right:0}
.title.teal{color:var(--teal)}
.tagline{font:400 8px 'Poiret One',sans-serif;color:var(--teal);text-align:center;left:0;right:0}
.sub{font:400 10px 'Poiret One',sans-serif;color:var(--teal)}
.sub.gold{color:var(--gold)}
.nm{font:600 3.7px 'Josefin Sans',sans-serif;color:var(--amber);text-transform:uppercase;letter-spacing:.15px;margin-top:3px}
.nm.light{font-weight:400;font-size:5px}
.ds{font:400 3.8px/1.3 'Cormorant Garamond',serif;color:var(--ink)}
.pr{font:400 3.6px 'Cormorant Garamond',serif;color:var(--sky)}
.tag{display:inline-block;font:600 2.6px 'Josefin Sans',sans-serif;color:#fff;padding:0 2px;border-radius:1px;vertical-align:middle;margin-left:1px}
.tag.cn,.tag.ca{background:var(--amber)}
.tag.cw{background:var(--sand);color:var(--ink)}
.tag.gf{background:var(--teal)}
.tag.v{background:var(--sky)}
.box{position:absolute;border:.7px solid var(--gold);border-radius:9px;padding:4px 7px}
.rows{font:400 3.7px 'Cormorant Garamond',serif;color:var(--sky)}
.rows div{display:flex;justify-content:space-between;gap:3px;line-height:1.45}
.rows .k{color:var(--amber);font-family:'Josefin Sans',sans-serif;font-size:3.3px;text-transform:uppercase}
.rows.teal .k{color:var(--teal)}
.rows .v{color:var(--sky)}
.cols3{display:flex;justify-content:space-between}
.cols3 > div{flex:1;text-align:center;padding:0 3px}
.cols3 > div + div{border-left:.6px solid var(--gold)}
.rule{position:absolute;left:0;right:0;margin:0 auto;width:120px;border-top:.6px dotted var(--teal)}
.legend{position:absolute;left:0;right:0;display:flex;justify-content:center;gap:6px;font:400 3.3px 'Cormorant Garamond',serif;color:var(--ink)}
.legend div{display:flex;flex-direction:column;gap:1px}
.legend span{display:flex;align-items:center;gap:2px;justify-content:flex-end}
.legend div+div span{justify-content:flex-start}
.band{position:absolute;left:0;right:0}
.band.teal{background:var(--teal)}
.band.mist{background:var(--mist)}
.on-teal .sub{color:#fff}
.on-teal .rows .k{color:#fff}
.on-teal .rows .v{color:#fff}
.pill{position:absolute;background:var(--sand);border-radius:6px;text-align:center;padding-top:2px}
.seasonal{position:absolute;left:50%;transform:translateX(-50%);border:1px solid #fff;outline:.6px solid var(--sand);outline-offset:1.5px;color:#fff;font:400 13px 'Josefin Sans',sans-serif;padding:2px 6px;letter-spacing:.5px}
.fanwall{position:absolute;left:0;right:0;background:linear-gradient(180deg,#7fc2c6,#3c9aa5)}
.ruled-title{display:flex;align-items:center;justify-content:center;gap:4px}
.ruled-title::before,.ruled-title::after{content:"";width:22px;border-top:.6px solid var(--teal)}
</style>
</head>
<body>
<div class="sheet">

<!-- Page 1: All Day Brunch -->
<section class="page teal" style="left:127px;top:26px">
  <div class="field">
    <div class="arch">
      <div class="logo"><span class="dot"></span><span class="name">BRIO WELDON</span></div>
      <h1 class="abs title" style="top:47px">ALL DAY BRUNCH</h1>
      <div class="abs tagline ruled-title" style="top:63px">Unique Flavors</div>
      <div class="abs cols3" style="top:80px;left:22px;right:22px">
        <div><div class="nm light">Grilled Cheese Sandwich</div><p class="ds">Big chou bun, 2 slices of fontina cheese, ham and bacon — the ultimate grilled cheese sandwich</p><p class="pr">$14.00</p></div>
        <div><div class="nm light">Croque Monsieur</div><p class="ds">Big chou bun served hot filled with creamy bechamel sauce, gruyère cheese, ham and bacon*</p><p class="pr">$15.00</p></div>
        <div><div class="nm light">Croque Madame</div><p class="ds">Big chou bun served hot filled with creamy bechamel sauce, gruyère, ham, bacon and an egg sunny side up</p><p class="pr">$16.50</p></div>
      </div>
      <div class="abs sub" style="top:126px;left:34px">Eggcellent Choices</div>
      <div class="abs sub" style="top:126px;left:168px">Pancakes</div>
      <div class="box" style="top:142px;left:26px;width:111px;height:120px">
        <p class="ds center" style="font-size:3.2px">Also available: Gluten Free Bun</p>
        <div class="nm">Eggs Florentine</div><p class="ds">Chou bun topped with chive cream cheese, sauté spinach, 2 eggs and pink hollandaise sauce</p><p class="pr">$16.45</p>
        <div class="nm">Eggs Benedict</div><p class="ds">Chou bun topped whipped chive cream cheese, ham, 2 eggs, and pink hollandaise sauce</p><p class="pr">$16.45</p>
        <div class="nm">Avocado &amp; Eggs</div><p class="ds">Chou bun topped with chunky avocado smash, crumbled feta, 2 eggs, spicy honey, oil, chili flakes and sesame</p><p class="pr">$17.45</p>
        <div class="nm">Eggs Royal</div><p class="ds">Chou bun topped with whipped cream cheese, chives, smoked salmon, red onion, 2 eggs, pink hollandaise, sesame seeds</p><p class="pr">$18.50</p>
      </div>
      <div class="box" style="top:142px;left:146px;width:111px;height:120px">
        <div class="nm">O.M.G. Eggs &amp; Bacon</div><p class="ds">4 pancakes topped with grated gruyère, bacon, an egg sunny side up and a side of maple syrup</p><p class="pr">$16.50</p>
        <div class="nm">Classic Nocciella &amp; Berries</div><p class="ds">4 pancakes topped with Nocciella, fresh berries and whipped cream</p><p class="pr">$16.50</p>
        <div class="nm">Tropical Guava &amp; Cheese</div><p class="ds">4 pancakes topped with guava cream, cream cheese frosting, fresh raspberries and raspberry syrup</p><p class="pr">$16.00</p>
        <div class="nm">Oriental <span class="tag cn">CN</span></div><p class="ds">4 pancakes topped with orange cream, caramelized pistachios, crunchy phyllo, drizzled with honey cinnamon syrup</p><p class="pr">$14.50</p>
      </div>
      <div class="abs sub gold center" style="top:266px;left:0;right:0">Sides</div>
      <div class="abs" style="top:280px;left:82px;width:106px;display:flex;gap:10px">
        <div class="rows teal" style="flex:1"><div><span class="k">Eggs (1)</span><span class="v">$2.99</span></div><div><span class="k">Bacon (4 slices)</span><span class="v">$4.00</span></div><div><span class="k">Salmon</span><span class="v">$3.50</span></div><div><span class="k">Pancakes (2)</span><span class="v">$3.50</span></div></div>
        <div class="rows teal" style="flex:1"><div><span class="k">Avocado Smash</span><span class="v">$2.50</span></div><div><span class="k">Fruit Bowl</span><span class="v">$5.25</span></div><div><span class="k">Green Salad</span><span class="v">$3.50</span></div></div>
      </div>
      <p class="abs ds" style="top:303px;left:82px">* Also available: Turkey bacon, turkey ham</p>
      <div class="rule" style="top:312px"></div>
      <div class="legend" style="top:316px">
        <div><span>Contain Nut <i class="tag cn">CN</i></span><span>Contain Almond <i class="tag ca">CA</i></span><span>Contain Walnut <i class="tag cw">CW</i></span></div>
        <div><span><i class="tag gf">GF</i> Gluten Free</span><span><i class="tag v">V</i> Vegan</span></div>
      </div>
    </div>
  </div>
</section>

<!-- Page 2: Lunch -->
<section class="page teal" style="left:433px;top:26px">
  <div class="field">
    <div class="arch">
      <div class="logo"><span class="dot"></span><span class="name">BRIO WELDON</span></div>
      <h1 class="abs title" style="top:50px">LUNCH</h1>
      <div class="abs sub" style="top:60px;left:58px">Salads</div>
      <div class="abs sub" style="top:60px;left:172px">Soups</div>
      <div class="box" style="top:78px;left:16px;width:111px;height:80px">
        <div class="nm">Greek</div><p class="ds">Baby tomatoes, cucumbers, feta, olives, onions, P.O.V. olive oil, vinegar</p><p class="pr">$5.50</p>
        <div class="nm">Garden Roquefort</div><p class="ds">Baby greens, arugula, beets, Roquefort blue cheese, caramelized pistachios, strawberries, orange vinaigrette</p><p class="pr">$5.50</p>
        <div class="nm">Zucchini</div><p class="ds">Fresh spiralized zucchini with feta, mint, almonds, lemon, POV olive oil</p><p class="pr">$6.55</p>
      </div>
      <div class="box" style="top:78px;left:137px;width:111px;height:80px">
        <div class="nm">French Onion Soup</div><p class="ds">Classic onion soup gratinated with gruyere cheese and crunchy eclairs</p><p class="pr">$7.95</p>
        <div class="nm">Pumpkin Soup</div><p class="ds">Homemade pumpkin soup served with cream and crushed chickpeas</p><p class="pr">$6.60</p>
        <div class="nm">Tomato Soup</div><p class="ds">Tomato soup served with prosciutto gruyere cheese and crunchy eclairs</p><p class="pr">$7.60</p>
      </div>
      <div class="band mist cols3" style="top:166px;height:38px;padding:5px 14px">
        <div><div class="nm light">Quiches</div><p class="ds">(available also in GF crust) Lorraine Mushroom Spinach Salmon tomato</p><p class="pr">$6.99</p></div>
        <div><div class="nm light">Phyllo Pocket</div><p class="ds">Feta cheese served hot drizzled with honey and sesame</p><p class="pr">$4.60</p></div>
        <div><div class="nm light">Brioches</div><p class="ds">Ham and cheese Feta and thyme</p><p class="pr">$4.30</p></div>
      </div>
      <h2 class="abs title" style="top:209px">VEGAN TREATS <span class="tag v">V</span></h2>
      <div class="abs sub" style="top:227px;left:34px">Cookies</div>
      <div class="abs sub" style="top:227px;left:109px">Muffins</div>
      <div class="abs sub" style="top:227px;left:186px">Verrines</div>
      <div class="abs rows" style="top:240px;left:34px;width:66px"><div><span class="k">Chocolate Chip</span><span class="v">$3.50</span></div><div><span class="k">Double Chocolate Chip</span><span class="v">$3.50</span></div><div><span class="k">Oatmeal Cinnamon</span><span class="v">$3.50</span></div><div><span class="k">Mini Cookies (3 pack)</span><span class="v">$3.10</span></div></div>
      <div class="abs rows" style="top:240px;left:106px;width:72px"><div><span class="k">Banana Chocolate Chip</span><span class="v">$3.00</span></div><div><span class="k">Chocolate/Choc Chips</span><span class="v">$3.00</span></div><div><span class="k">Blueberry</span><span class="v">$3.00</span></div><div><span class="k">Banana Walnut (CN)</span><span class="v">$3.00</span></div></div>
      <div class="abs rows" style="top:240px;left:184px;width:66px"><div><span class="k">Chocolate Cake (GF)</span><span class="v">$6.75</span></div><div><span class="k">Lemon Berries (GF)</span><span class="v">$6.75</span></div><div><span class="k">Coconut Cake (GF)</span><span class="v">$6.75</span></div></div>
      <div class="abs cols3" style="top:266px;left:60px;right:40px">
        <div><div class="nm light">Florentine</div><p class="ds">Chou bun topped with vegan creamy cheese with garlic &amp; herbs, sauté spinach, 2 omelettes</p><p class="pr">$12.45</p></div>
        <div><div class="nm light">Avocado Toast</div><p class="ds">Chou bun topped with vegan creamy cheese with garlic and herbs, avocado smash, sliced tomatoes, microgreens &amp; sesame seeds, served with a side of spicy honey</p><p class="pr">$15.45</p></div>
      </div>
      <div class="rule" style="top:312px"></div>
      <div class="legend" style="top:316px">
        <div><span>Contain Nut <i class="tag cn">CN</i></span><span>Contain Almond <i class="tag ca">CA</i></span><span>Contain Walnut <i class="tag cw">CW</i></span></div>
        <div><span><i class="tag gf">GF</i> Gluten Free</span><span><i class="tag v">V</i> Vegan</span></div>
      </div>
    </div>
  </div>
</section>

<!-- Page 3: Sweet Eclairs -->
<section class="page gold" style="left:127px;top:413px">
  <div class="field">
    <div class="arch">
      <div class="logo"><span class="dot"></span><span class="name">BRIO WELDON</span></div>
      <h1 class="abs title" style="top:44px">SWEET ECLAIRS</h1>
      <div class="abs sub" style="top:62px;left:34px">Single</div>
      <div class="abs sub" style="top:62px;left:147px">Double</div>
      <div class="abs" style="top:74px;left:34px;width:112px">
        <div class="nm">Chocolate Éclair</div><p class="ds">the classic chocolate: pastry filling with chocolate glaze</p><p class="pr">$5.20 <i class="tag gf">GF</i><i class="tag v">V</i> Available</p>
        <div class="nm">Vanilla Éclair</div><p class="ds">the classic: vanilla pastry filling with chocolate glaze</p><p class="pr">$5.20 <i class="tag gf">GF</i><i class="tag v">V</i> Available</p>
        <div class="nm">Coffee Éclair</div><p class="ds">Coffee creamy filling with a Caramel Coffee Glaze</p><p class="pr">$5.20</p>
        <div class="nm">Tres Leches Éclair</div><p class="ds">Tres leches cream perfumed with real rum and cinnamon, glaze in white chocolate</p><p class="pr">$5.20 <i class="tag gf">GF</i><i class="tag v">V</i> Available</p>
        <div class="nm">Guava Éclair</div><p class="ds">the guava pastry filling with pink sweet glaze</p><p class="pr">$5.20 <i class="tag gf">GF</i><i class="tag v">V</i></p>
        <div class="nm">Strawberry Éclair</div><p class="ds">the vanilla pastry cream and strawberry jam, dipped in red glaze</p><p class="pr">$5.20</p>
        <div class="nm">Creme Brulee Éclair</div><p class="ds">filled with classic vanilla pastry cream and dipped in hard caramel</p><p class="pr">$5.20</p>
      </div>
      <div class="abs" style="top:74px;left:147px;width:108px">
        <div class="nm">German Chocolate Éclair <i class="tag cn">CN</i></div><p class="ds">Chocolate cream filling topped with a rich sticky coconut and pecan paste dipped in hard dark chocolate with touches of gold</p><p class="pr">$5.70</p>
        <div class="nm">Tiramisu Éclair</div><p class="ds">Double éclair filled with vanilla custard cream flavored with espresso coffee cream, topped with mascarpone cream and lady fingers cake</p><p class="pr">$5.70</p>
        <div class="nm">Baklava Éclair <i class="tag cn">CN</i></div><p class="ds">Filled with orange pastry cream, decorated with caramelized pistachios and pieces of fyllo dough drizzled with honey and cinnamon</p><p class="pr">$5.70</p>
        <div class="nm">Tropical Passion Éclair</div><p class="ds">Double éclair filled with mango pastry cream topped with light passion fruit panna cotta with an insert of mango gelée</p><p class="pr">$5.70</p>
      </div>
      <div class="pill" style="top:211px;left:147px;width:100px;height:20px">
        <div class="sub" style="color:var(--ink);font-size:8px;line-height:8px">Meringues</div>
        <div class="nm" style="color:var(--ink);margin-top:1px;font-size:3px">Meringue Box $3.70</div>
      </div>
      <div class="band teal on-teal" style="top:238px;height:76px">
        <div class="abs sub" style="top:4px;left:26px">Bread Puddings <i class="tag cn">CN</i></div>
        <div class="abs rows" style="top:18px;left:26px;width:100px"><div><span class="k">Mango &amp; White Chocolate <i class="tag ca">CA</i></span><span class="v">$5.20</span></div><div><span class="k">Guava <i class="tag ca">CA</i></span><span class="v">$5.20</span></div><div><span class="k">Brownie Walnut <i class="tag cw">CW</i></span><span class="v">$5.20</span></div><div><span class="k" style="color:var(--sand)">Add a scoop of vanilla ice-cream</span><span class="v">+$2.50</span></div></div>
        <div class="abs sub" style="top:4px;left:144px">Macarons <i class="tag ca">CA</i></div>
        <div class="abs" style="top:18px;left:144px;width:105px;font:600 3.3px/1.35 'Josefin Sans',sans-serif;color:#fff">WHITE CHOCOLATE | DARK CHOCOLATE | LEMON | APRICOT | RASPBERRY | PISTACHIO <span style="color:var(--sand)">(CONTAINS PISTACHIO AND ALMOND)</span><br>$3.20</div>
        <div class="abs center" style="top:43px;left:0;right:0;border-top:.6px dotted #fff;margin:0 30px;padding-top:2px">
          <div class="sub" style="font-size:9.5px">Cake Pops</div>
          <div style="font:600 3.3px 'Josefin Sans',sans-serif;color:#fff;margin-top:2px">VANILLA | CHOCOLATE | CARROT CAKE | V G.F. BROWNIE <span style="color:var(--sand)">(CONTAINS CHICKPEAS)</span><br>$3.50</div>
        </div>
      </div>
      <div class="legend" style="top:318px">
        <div><span>Contain Nut <i class="tag cn">CN</i></span><span>Contain Almond <i class="tag ca">CA</i></span><span>Contain Walnut <i class="tag cw">CW</i></span></div>
        <div><span><i class="tag gf">GF</i> Gluten Free</span><span><i class="tag v">V</i> Vegan</span></div>
      </div>
    </div>
  </div>
</section>

<!-- Page 4: Savory Eclairs -->
<section class="page gold" style="left:433px;top:413px">
  <div class="field">
    <div class="arch">
      <div class="logo"><span class="dot"></span><span class="name">BRIO WELDON</span></div>
      <h1 class="abs title teal" style="top:44px">SAVORY ECLAIRS</h1>
      <p class="abs nm center" style="top:58px;left:0;right:0">Side of green salad + $3.50</p>
      <div class="abs sub gold" style="top:68px;left:22px">Hot</div>
      <div class="abs sub gold" style="top:68px;left:138px">Cold</div>
      <div class="abs" style="top:80px;left:22px;width:108px">
        <div class="nm" style="color:var(--teal)">Shepperd's Pie Éclair</div><p class="ds">Seasoned ground beef, topped with creamy mashed potatoes, and grated parmesan cheese</p><p class="pr">$9.55</p>
        <div class="nm" style="color:var(--teal)">Chicken, Spinach, Artichoke Éclair</div><p class="ds">Rich cream with spinach chicken and artichoke hearts, gratinated with parmesan, gruyere and gouda cheese</p><p class="pr">$9.75</p>
        <div class="nm" style="color:var(--teal)">Mushroom Éclair</div><p class="ds">Creamy mashed potatoes, sautéed mushrooms, shaved Parmesan flakes, truffle oil, and chives</p><p class="pr">$9.75</p>
        <div class="nm" style="color:var(--teal)">Sweet Brie Éclair</div><p class="ds">Melted brie, arugula, strawberry sauce and fresh strawberry halves</p><p class="pr">$9.75</p>
      </div>
      <div class="abs" style="top:80px;left:138px;width:108px">
        <div class="nm">Tuna Salad Éclair</div><p class="ds">Classic tuna salad with refreshing grapes and celery.</p><p class="pr">$7.55</p>
        <div class="nm">Caprese Éclair</div><p class="ds">Mozzarella cream, baby tomatoes and mozzarella pearls, topped with fresh basil and balsamic vinegar glaze</p><p class="pr">$7.55</p>
        <div class="nm">Roquefort Dream Éclair <i class="tag cn">CN</i></div><p class="ds">Roquefort cream, Prosciutto, glazed pear wedges, and crushed caramelized pistachios drizzled with Balsamic fig glaze</p><p class="pr">$9.75</p>
        <div class="nm">Smoked Salmon Éclair</div><p class="ds">Whipped cream cheese with chives, smoked salmon, dill, tomatoes and onions</p><p class="pr">$9.75</p>
      </div>
      <div class="band teal" style="top:198px;height:120px">
        <div class="seasonal" style="top:10px">SEASONAL</div>
        <div class="fanwall" role="img" aria-label="Art deco fan arch pattern in soft teal tones" style="top:72px;height:48px"></div>
      </div>
      <div class="legend" style="top:322px">
        <div><span>Contain Nut <i class="tag cn">CN</i></span><span>Contain Almond <i class="tag ca">CA</i></span><span>Contain Walnut <i class="tag cw">CW</i></span></div>
        <div><span><i class="tag gf">GF</i> Gluten Free</span><span><i class="tag v">V</i> Vegan</span></div>
      </div>
    </div>
  </div>
</section>

<!-- Page 5: Petits Gateaux -->
<section class="page teal" style="left:127px;top:801px">
  <div class="field">
    <div class="arch">
      <div class="logo"><span class="dot"></span><span class="name">BRIO WELDON</span></div>
      <h1 class="abs title" style="top:49px">PETITS GATEAUX</h1>
      <div class="abs" style="top:66px;left:28px;width:104px">
        <div class="nm" style="color:var(--teal)">Pumpkin Cheesecake</div><p class="ds">New Fall favorite: pumpkin cheesecake served with whipped cream and drizzled with caramel</p><p class="pr">$6.90</p>
        <div class="nm" style="color:var(--teal)">Chocolate Raspberry Kiss <i class="tag gf">GF</i></div><p class="ds">Chocolate mousse with a raspberry cremeux center, on a chocolate cookie</p><p class="pr">$5.70</p>
        <div class="nm" style="color:var(--teal)">Caramel Strawberry</div><p class="ds">Runny strawberry gelee heart on a merengue cookie enrobed with light dulcey caramel mousse</p><p class="pr">$6.90</p>
        <div class="nm" style="color:var(--teal)">NY Cheesecake Classic</div><p class="ds">Cheesecake made of Delmont cream cheese on a graham cracker</p><p class="pr">$6.90</p>
        <div class="nm" style="color:var(--teal)">Key Lime Mango</div><p class="ds">Key lime cream with the sweetness of the mango gelee with a graham cracker insert</p><p class="pr">$6.90</p>
      </div>
      <div class="abs" style="top:66px;left:146px;width:108px">
        <div class="nm" style="color:var(--teal)">Pavlova <i class="tag gf">GF</i></div><p class="ds">Pink crispy meringue nest, filled with a light pistachio cream, pieces of fresh strawberries in red fruit gelee and topped with fluffy whipped cream &amp; caramelized pistachios.</p><p class="pr">$7.50</p>
        <div class="nm" style="color:var(--teal)">Napoleon Millefeuille</div><p class="ds">Indulge in the exquisite layers of delicate flaky pastry, velvety vanilla pastry cream filling, and airy chantilly that make our Millefeuille a true masterpiece</p><p class="pr">$7.30</p>
        <div class="nm" style="color:var(--teal)">Sunset Kiss <i class="tag cn">CN</i></div><p class="ds">Airy passion fruit panna cotta with an insert of almond biscuit and a heart of mango cremeux dipped in yellow mirror glaze, surrounded by white and yellow chocolate, on a vanilla cookie</p><p class="pr">$8.50</p>
      </div>
      <div class="abs" style="top:175px;left:146px;width:96px;height:128px;background:var(--mist);border:.6px solid var(--gold);border-radius:12px 12px 4px 4px;padding:4px 6px">
        <div class="title teal" style="position:static;font-size:12px">TARTS</div>
        <div class="nm">Key Lime Tart</div><p class="ds">Classic Key lime tart made of lime juice from the Keys with meringue rosettes</p><p class="pr">$7.95</p>
        <div class="nm">La Vie En Rose <i class="tag ca">CA</i></div><p class="ds">Vanilla tart filled with almond frangipane cream and topped with an airy pineapple passionfruit mousse in the shape of a velvety rose</p><p class="pr">$8.80</p>
        <div class="nm">Fruit Tart</div><p class="ds">Sweet vanilla tart filled with vanilla cream and topped with fresh berries and seasonal fruits</p><p class="pr">$7.95</p>
        <div class="nm">Fruit Tart</div><p class="ds">Pistachio joconde cake layered with pistachio buttercream, chocolate ganache &amp; raspberry gelée.</p><p class="pr">$8.80</p>
      </div>
      <div class="abs" style="top:220px;left:26px;width:110px;border-top:.6px dotted var(--teal)"></div>
      <h2 class="abs title teal" style="top:224px;left:26px;right:auto;font-size:12px">TRAVEL CAKES <span class="tag v">V</span></h2>
      <div class="abs rows" style="top:240px;left:32px;width:78px"><div><span class="k">Banana Pecan <i class="tag cn">CN</i></span><span class="v">$6.00</span></div><div><span class="k">Banana Walnut <i class="tag cw">CW</i></span><span class="v">$6.00</span></div><div><span class="k">Banana Chocolate Chips</span><span class="v">$6.00</span></div><div><span class="k">Blueberry</span><span class="v">$6.00</span></div></div>
      <h2 class="abs title" style="top:266px;left:26px;right:auto;font-size:12px">BABA AU RHUM</h2>
      <div class="abs rows teal" style="top:281px;left:40px;width:80px"><div><span class="k" style="color:var(--sky)">Contain alcohol</span></div><div><span class="k">Chocolate / Nocciella</span><span class="v">$7.80</span></div><div><span class="k">Vanilla/Orange/Pineapples</span><span class="v">$7.80</span></div></div>
      <div class="rule" style="top:312px"></div>
      <div class="legend" style="top:316px">
        <div><span>Contain Nut <i class="tag cn">CN</i></span><span>Contain Almond <i class="tag ca">CA</i></span><span>Contain Walnut <i class="tag cw">CW</i></span></div>
        <div><span><i class="tag gf">GF</i> Gluten Free</span><span><i class="tag v">V</i> Vegan</span></div>
      </div>
    </div>
  </div>
</section>

<!-- Page 6: Mocktails & Beverages -->
<section class="page teal" style="left:433px;top:801px">
  <div class="field" style="--field:var(--cream)">
    <div class="arch mist">
      <div class="logo"><span class="dot"></span><span class="name">BRIO WELDON</span></div>
      <h1 class="abs title teal" style="top:49px">MOCKTAILS</h1>
      <div class="abs cols3" style="top:64px;left:20px;right:20px">
        <div><div class="nm light">Pina Colada</div><p class="ds">A tropical classic mocktail of pineapple and coconut</p><p class="pr">$6.30</p></div>
        <div><div class="nm light">Mango Lychee</div><p class="ds">Refreshing mix of lychee &amp; mango</p><p class="pr">$6.50</p></div>
        <div><div class="nm light">Ruby Temple</div><p class="ds">Ginger ale and grenadine mocktail garnished with maraschino cherry.</p><p class="pr">$6.30</p></div>
      </div>
      <h2 class="abs title teal" style="top:96px">COFFEES &amp; BEVERAGES</h2>
      <div class="abs sub gold" style="top:112px;left:26px">Hot Coffee</div>
      <div class="abs sub gold" style="top:112px;left:110px">Iced Coffee</div>
      <div class="abs sub gold" style="top:112px;left:187px">Matcha</div>
      <div class="abs rows" style="top:126px;left:26px;width:62px"><div><span class="k">Filter Coffee</span><span class="v">$2.40</span></div><div><span class="k">Espresso</span><span class="v">$2.75</span></div><div><span class="k">Cappuccino</span><span class="v">$3.50</span></div><div><span class="k">Latte</span><span class="v">$3.70</span></div><div><span class="k">Americano</span><span class="v">$3.00</span></div><div><span class="k">Espresso Macchiato</span><span class="v">$3.00</span></div></div>
      <div class="abs rows" style="top:126px;left:110px;width:60px"><div><span class="k">Iced Espresso</span><span class="v">$4.00</span></div><div><span class="k">Iced Cappuccino</span><span class="v">$4.55</span></div><div><span class="k">Iced Latte</span><span class="v">$4.70</span></div></div>
      <div class="abs rows" style="top:126px;left:187px;width:62px"><div><span class="k">Matcha Tea</span><span class="v">$3.20</span></div><div><span class="k">Matcha Latte Hot</span><span class="v">$3.95</span></div><div><span class="k">Matcha Latte Cold</span><span class="v">$3.95</span></div></div>
      <div class="box" style="top:167px;left:22px;width:230px;height:35px;background:var(--cream);padding:2px 6px;text-align:center">
        <div class="sub gold" style="font-size:9px">Coffee Syrups - Sauces - Toppings - Ginger</div>
        <p style="font:600 3.2px/1.4 'Josefin Sans',sans-serif;color:var(--ink);margin-top:2px">VANILLA | HAZELNUT | CARAMEL | MOCHA | LAVENDER | ALMOND (ASK FOR OUR SUGAR FREE OPTIONS) <span style="color:var(--amber)">+$1.00</span><br>DARK OR WHITE CHOCOLATE SAUCE <span style="color:var(--amber)">+$1.00</span> EXTRA SHOT <span style="color:var(--amber)">+$1.00</span> DECAF <span style="color:var(--amber)">+$1.00</span></p>
      </div>
      <div class="abs sub gold" style="top:214px;left:60px">Tea</div>
      <div class="abs sub gold" style="top:214px;left:144px">Cold Drinks</div>
      <div class="abs rows teal" style="top:228px;left:60px;width:72px"><div><span class="k">Earl Grey</span><span class="v">$3.50</span></div><div><span class="k">Darjeeling</span><span class="v">$3.50</span></div><div><span class="k">Ginger Lemongrass</span><span class="v">$3.50</span></div><div><span class="k">Camomile</span><span class="v">$3.50</span></div><div><span class="k">Mint Vervain &amp; Herbs</span><span class="v">$3.50</span></div><div><span class="k">Fruit Symphony</span><span class="v">$3.50</span></div><div><span class="k">Dragon Sencha Green Tea</span><span class="v">$3.50</span></div><div><span class="k">Iced Tea</span><span class="v">$3.50</span></div></div>
      <div class="abs rows teal" style="top:228px;left:144px;width:70px"><div><span class="k">Isla Water 16 oz</span><span class="v">$3.70</span></div><div><span class="k">San Vallino</span><span class="v">$4.70</span></div><div><span class="k">Koala Cola / Diet</span><span class="v">$4.00</span></div><div><span class="k">Perlaine</span><span class="v">$4.70</span></div><div><span class="k">Homemade Lemonade</span><span class="v">$6.50</span></div><div><span class="k">Mint Lemonade</span><span class="v">$6.50</span></div><div><span class="k">Strawberry Lemonade</span><span class="v">$6.50</span></div><div><span class="k">Lavender Lemonade</span><span class="v">$6.50</span></div><div><span class="k">Orange Juice</span><span class="v">$4.70</span></div></div>
      <div class="abs sub gold" style="top:280px;left:112px">Chocolate</div>
      <div class="abs rows teal" style="top:294px;left:112px;width:52px"><div><span class="k">Chocolate Hot</span><span class="v">$4.95</span></div><div><span class="k">Chocolate Cold</span><span class="v">$4.95</span></div><div><span class="k">Whipped Cream</span><span class="v">+1.00</span></div></div>
    </div>
  </div>
</section>

</div>
</body>
</html>
```